Single Landing Page Redesign - CRO Experts Welcome!

We need our landing page redesigned. We will be giving a lot of weight to conversion optimization so be sure to redesign the landing page with conversion optimization concepts in mind.

This is the landing page that needs to be redesigned:
http://www.pagecrateworks.example/message_board/forum3.html

Here are some ideas that we think could increase conversions in order of priority:

- Show a screenshot of an example forum, linked to the forum's address (http://forums.mindlantern.example/)

- Change the "Get Feedback from Users" feature to "Mobile Friendly (perhaps a picture of an iphone with a mobile version of our forum loaded in it? - mobile version isn't launched yet)

- Mention "Social Sharing" as a feature. (perhaps mention something about content going viral?)

- Additional testimonials:
"Pagecrate Works has been a superb solution for GoldenVow Journeys. Our customers love it-and the customization available is flexible enough to allow us to "brand" the forums so that they fit with our main site. Tech support has been outstanding, with quick & helpful responses to the questions we've had."
Daniel Ferrow
www.goldenvow.example

"Very simple and easy to set up, yet so customizable. It looks like it resides right on our site."
Tobias Wendling
www.pvtrsa.example

- Additional client logo: swiftrail coaches (swiftrail.example) - It would be better if logos are in a horizontal line in gray.

- Benefits of creating a forum (paragraph or bullet points or any other creative way): Running a forum is an excellent way of creating a community. It can be a place for people to discuss issues, share knowledge, and talk about you, your product, or your service. In the long-term, providing a way for your users to be part of a community can prove to be invaluable in terms of search engine optimization, customer satisfaction, customer/visitor retention, brand awareness, customer support, viral promotion, building trust, and creating a new revenue stream.

- Additional info that can be included, which might increase conversions (not mandatory) (can be reworded or changed as needed):
Embed your forum into an existing website in seconds!
Cloud-Based
Secure - Our forums are equipped with security features that make hackers and spammers a thing of the past.

You are welcome to implement your own ideas as well.

Nice landing pages:
http://www.trymeadowly.example/ (I love the big, wide design.)
http://www.quarnix.example/crm/

The physical layout of the page can be changed completely. The existing text and elements of the landing page can be changed completely. None of the existing landing page has to remain the way it is. Be creative and come up with what you think looks best. The existing landing page is only an example of what we currently have.

The PSD of our logo is attached.

We look forward to seeing your mockups!

```html
<!DOCTYPE html>
<html lang="en">
<head>
<meta charset="utf-8">
<title>Pagecrate Works – Create a Powerful Forum</title>
<link href="https://fonts.googleapis.com/css2?family=Lato:wght@300;400;700;900&display=swap" rel="stylesheet">
<style>
:root{
  --ink:#2f3a45;
  --muted:#7b8691;
  --brand:#1d7cc1;
  --brand-dark:#16679f;
  --navy:#1f3550;
  --orange:#f28a2e;
  --hero-a:#6f8fa8;
  --hero-b:#9fb7c8;
  --light:#eef1f4;
  --card:#ffffff;
  --line:#d9dee3;
  --footer:#2c3640;
  --footer-text:#aeb7bf;
  --logo-grey:#9aa2a9;
}
*{box-sizing:border-box;margin:0;padding:0}
html,body{width:698px;height:1200px;overflow:hidden}
body{font-family:"Lato",Arial,sans-serif;color:var(--ink);background:#fff;font-size:8px;line-height:1.4}
.page{width:698px;height:1200px;position:relative}

/* header */
.site-header{height:33px;display:flex;align-items:center;justify-content:space-between;padding:0 40px 0 34px;border-bottom:1px solid var(--line)}
.brand{display:flex;align-items:center;gap:5px;font-weight:900;font-size:13px;color:var(--brand)}
.brand-mark{width:12px;height:12px;background:var(--brand);border-radius:50%}
.header-right{display:flex;flex-direction:column;align-items:flex-end;gap:3px}
.utility{display:flex;gap:12px;font-size:6.5px;color:var(--muted)}
.nav{display:flex;gap:0}
.nav a{font-size:6.5px;font-weight:700;color:var(--ink);text-decoration:none;padding:3px 10px;letter-spacing:.3px}
.nav a.active{background:var(--brand);color:#fff}

/* hero */
.hero{height:223px;position:relative;background:linear-gradient(120deg,var(--hero-a),var(--hero-b));color:#fff;padding:22px 0 0 80px}
.hero-arrow{position:absolute;top:96px;width:14px;height:22px}
.hero-arrow.left{left:16px}.hero-arrow.right{right:16px}
.hero h1{font-size:21px;font-weight:900;line-height:1.12;letter-spacing:.3px;width:300px}
.hero .tagline{font-size:10px;font-weight:300;margin:6px 0 12px}
.hero-points{display:grid;grid-template-columns:88px 100px;gap:4px 10px;list-style:none;font-size:7px;margin-bottom:16px}
.hero-points li::before{content:"✓ ";color:#fff;font-weight:900}
.cta{display:inline-block;background:var(--orange);color:#fff;font-weight:700;font-size:9px;padding:8px 20px;border-radius:3px;text-decoration:none}
.hero .fine{font-size:6px;font-style:normal;opacity:.85;margin-top:6px}
.hero-screen{position:absolute;right:66px;top:26px;width:232px;height:178px;background:linear-gradient(180deg,#dfe7ee,#b8c6d1);border-radius:4px;border:6px solid #1e252c;border-bottom-width:18px}
.hero-stand{position:absolute;right:160px;top:204px;width:44px;height:14px;background:#c8cfd5}

/* features */
.features{height:339px;background:var(--brand);color:#fff;text-align:center;padding:24px 70px 0}
.section-title{font-size:14px;font-weight:700}
.features .rule{width:40px;height:2px;background:#fff;margin:5px auto 22px;opacity:.6}
.feature-grid{display:grid;grid-template-columns:repeat(3,1fr);gap:24px 40px}
.feature-icon{width:40px;height:40px;border-radius:50%;background:var(--navy);margin:0 auto 8px;display:flex;align-items:center;justify-content:center}
.feature h3{font-size:9px;font-weight:700;margin-bottom:4px}
.feature p{font-size:6px;line-height:1.5;opacity:.85}

/* video */
.video{height:233px;background:var(--light);padding:18px 46px 0}
.video .section-title{color:var(--ink);margin-bottom:10px}
.video-row{display:flex;gap:28px}
.video-frame{width:300px;height:164px;background:linear-gradient(180deg,#bfe3f0,#e6d6b8);position:relative;border-radius:2px}
.video-play{position:absolute;left:130px;top:62px;width:40px;height:40px;border-radius:50%;background:rgba(20,30,40,.7);display:flex;align-items:center;justify-content:center}
.video-bar{position:absolute;left:0;right:0;bottom:0;height:12px;background:#222}
.video-copy{flex:1}
.video-copy h3{font-size:9.5px;font-weight:700;line-height:1.35;margin-bottom:8px}
.video-copy ul{list-style:none}
.video-copy li{font-size:6.5px;color:#4c5862;margin-bottom:5px;padding-left:8px;position:relative}
.video-copy li::before{content:"";position:absolute;left:0;top:3px;width:3px;height:3px;background:var(--brand);border-radius:50%}

/* testimonials */
.testimonials{height:197px;padding:16px 46px 0;text-align:center}
.testimonials .section-title{color:var(--brand)}
.testimonials .sub{font-size:6.5px;color:var(--muted);margin:3px 0 16px}
.quote-grid{display:grid;grid-template-columns:repeat(3,1fr);gap:26px}
.quote-card{border:1px solid var(--line);background:var(--card);padding:10px;font-size:6.5px;color:#56616b;min-height:78px;position:relative}
.quote-card::after{content:"";position:absolute;left:50%;bottom:-6px;width:10px;height:10px;background:#fff;border-right:1px solid var(--line);border-bottom:1px solid var(--line);transform:translateX(-50%) rotate(45deg)}
.quote-author{margin-top:12px;font-size:7px}
.quote-author strong{display:block;font-weight:700;color:var(--ink)}
.quote-author span{color:var(--muted);font-size:6px}

/* clients */
.clients{height:118px;text-align:center;padding-top:4px}
.clients .section-title{color:var(--brand)}
.clients .sub{font-size:6.5px;color:var(--muted);margin:3px 0 16px}
.client-row{display:flex;justify-content:center;gap:30px;align-items:center}
.client{font-size:14px;font-weight:700;color:var(--logo-grey)}

/* footer */
.site-footer{height:57px;background:var(--footer);color:var(--footer-text);padding:12px 46px 0}
.footer-row{display:flex;justify-content:space-between;align-items:center}
.footer-links{display:flex;gap:12px;font-size:7px}
.subscribe{display:flex;margin-top:6px}
.subscribe input{width:120px;height:14px;border:0;font:6px "Lato",sans-serif;padding:0 5px}
.subscribe button{height:14px;border:0;background:var(--orange);color:#fff;font:700 6px "Lato",sans-serif;padding:0 8px}
.social{display:flex;gap:5px;align-items:center;font-size:7px}
.social i{width:12px;height:12px;display:block;border-radius:2px}
.copyright{text-align:center;font-size:5.5px;margin-top:6px}
</style>
</head>
<body>
<div class="page">

<header class="site-header">
  <div class="brand"><span class="brand-mark"></span>Pagecrate Works</div>
  <div class="header-right">
    <div class="utility"><span>☎ (800) 555-0142</span><span>Live chat</span><span>Sign in</span></div>
    <nav class="nav"><a class="active" href="#">HOME</a><a href="#">FEATURES</a><a href="#">PRICING</a><a href="#">CONTACT US</a></nav>
  </div>
</header>

<section class="hero">
  <svg class="hero-arrow left" viewBox="0 0 14 22"><path d="M11 2 3 11l8 9" fill="none" stroke="#fff" stroke-width="3"/></svg>
  <svg class="hero-arrow right" viewBox="0 0 14 22"><path d="M3 2l8 9-8 9" fill="none" stroke="#fff" stroke-width="3"/></svg>
  <h1>THE EASIEST<br>WAY TO CREATE A<br>POWERFUL FORUM</h1>
  <p class="tagline">No Coding, Software, or Servers</p>
  <ul class="hero-points">
    <li>Instant Setup</li><li>Fully Customizable</li>
    <li>Public or Private</li><li>Monetization</li>
    <li>SEO Friendly</li><li>Moderation</li>
  </ul>
  <a class="cta" href="http://forums.mindlantern.example/">Create a Forum Now</a>
  <p class="fine">It's only takes a few seconds to sign up</p>
  <div class="hero-screen" role="img" aria-label="Screenshot of an example forum shown on a desktop monitor"></div>
  <div class="hero-stand"></div>
</section>

<section class="features">
  <h2 class="section-title">Whats included</h2>
  <div class="rule"></div>
  <div class="feature-grid">
    <div class="feature">
      <div class="feature-icon"><svg width="18" height="18" viewBox="0 0 18 18"><circle cx="9" cy="6" r="3.5" fill="#fff"/><path d="M2 17c0-4 3-6 7-6s7 2 7 6z" fill="#fff"/></svg></div>
      <h3>Login with Friendhub</h3>
      <p>Users can sign in with one click using their existing social account, no new password needed.</p>
    </div>
    <div class="feature">
      <div class="feature-icon"><svg width="18" height="18" viewBox="0 0 18 18"><path d="M2 3h14v9H7l-4 3v-3H2z" fill="#fff"/></svg></div>
      <h3>Use Friendhub-Style Chat</h3>
      <p>Members can chat with each other in real time through a familiar, simple chat bar.</p>
    </div>
    <div class="feature">
      <div class="feature-icon"><svg width="18" height="18" viewBox="0 0 18 18"><rect x="2" y="4" width="14" height="11" rx="1" fill="#fff"/><path d="M4 13l3-4 3 3 2-2 3 3z" fill="#1f3550"/></svg></div>
      <h3>Share Files, Photos and Videos</h3>
      <p>Upload and embed media right inside posts so content can be shared and spread fast.</p>
    </div>
    <div class="feature">
      <div class="feature-icon"><svg width="18" height="18" viewBox="0 0 18 18"><rect x="2" y="4" width="14" height="12" rx="1" fill="#fff"/><rect x="2" y="4" width="14" height="3" fill="#9fb7c8"/></svg></div>
      <h3>Announce and Organize Events</h3>
      <p>Post events on a shared calendar and keep your whole community informed.</p>
    </div>
    <div class="feature">
      <div class="feature-icon"><svg width="18" height="18" viewBox="0 0 18 18"><rect x="5" y="1" width="8" height="16" rx="1.5" fill="#fff"/><rect x="6.5" y="3" width="5" height="10" fill="#1f3550"/></svg></div>
      <h3>Mobile Friendly</h3>
      <p>Your forum adapts to phones and tablets so members can join in from anywhere.</p>
    </div>
    <div class="feature">
      <div class="feature-icon"><svg width="18" height="18" viewBox="0 0 18 18"><rect x="4" y="8" width="10" height="8" rx="1" fill="#fff"/><path d="M6 8V6a3 3 0 0 1 6 0v2" fill="none" stroke="#fff" stroke-width="1.6"/></svg></div>
      <h3>Set User Permissions</h3>
      <p>Control who can read, post and moderate with flexible group permissions.</p>
    </div>
  </div>
</section>

<section class="video">
  <h2 class="section-title">Watch our Video</h2>
  <div class="video-row">
    <div class="video-frame" role="img" aria-label="Explainer video still of an animated scene">
      <div class="video-play"><svg width="14" height="16" viewBox="0 0 14 16"><path d="M2 1l11 7-11 7z" fill="#fff"/></svg></div>
      <div class="video-bar"></div>
    </div>
    <div class="video-copy">
      <h3>Pagecrate Works proudly serves over 100 million visits per month to over 15,000 forums</h3>
      <ul>
        <li>Running a forum is an excellent way of creating a community. It can be a place for people to discuss issues, share knowledge, and talk about you.</li>
        <li>Embed your forum into an existing website in seconds!</li>
        <li>Cloud-Based</li>
        <li>Secure – Our forums are equipped with security features that make hackers a thing of the past.</li>
        <li>Systems running 24 hours a day</li>
      </ul>
    </div>
  </div>
</section>

<section class="testimonials">
  <h2 class="section-title">What our customers said about our service</h2>
  <p class="sub">Real feedback from forum owners who build their communities with us every day.</p>
  <div class="quote-grid">
    <div>
      <div class="quote-card">“Excellent customer service, amazing features and reliable uptime. Our members love the forum and it was running in minutes.”</div>
      <div class="quote-author"><strong>Lena Marsh</strong><span>www.lenamarsh.example</span></div>
    </div>
    <div>
      <div class="quote-card">“Pagecrate Works has been a superb solution for GoldenVow Journeys. Our customers love it and tech support has been outstanding.”</div>
      <div class="quote-author"><strong>Daniel Ferrow</strong><span>www.goldenvow.example</span></div>
    </div>
    <div>
      <div class="quote-card">“Very simple and easy to set up, yet so customizable. It looks like it resides right on our site.”</div>
      <div class="quote-author"><strong>Tobias Wendling</strong><span>www.pvtrsa.example</span></div>
    </div>
  </div>
</section>

<section class="clients">
  <h2 class="section-title">Featured Clients</h2>
  <p class="sub">Pagecrate Works proudly serves over 100 million visits per month to over 15,000 forums.</p>
  <div class="client-row">
    <span class="client">Marelle</span>
    <span class="client">swiftrail coaches</span>
    <span class="client">Verdane</span>
    <span class="client">foxlight</span>
    <span class="client">Northwave News</span>
    <span class="client">brightly</span>
  </div>
</section>

<footer class="site-footer">
  <div class="footer-row">
    <div>
      <div class="footer-links"><span>Home</span><span>Features</span><span>Pricing</span><span>Contact</span></div>
      <form class="subscribe"><input type="email" placeholder="Enter your email"><button type="button">Subscribe</button></form>
    </div>
    <div class="social">Follow Us
      <i style="background:#3b5998"></i><i style="background:#e1306c"></i><i style="background:#f28a2e"></i><i style="background:#1da1f2"></i><i style="background:#2a7ab0"></i>
    </div>
  </div>
  <p class="copyright">Copyright © Pagecrate Works. All rights reserved.</p>
</footer>

</div>
</body>
</html>
```